Would like a Northwest feel to the look, something NOT typical of what you would see on a typical Home Inspectors logo. Real estate cards all the same as well, and would like to stand out. Earthy, green, Northwest. Sadly a portrait seems to be a requirement (see the attached). I inspect residential homes for buyers and sellers.

Target Market(s)

Home Buyers and Sellers

Industry/Entity Type

Home Inspection

Contact Information for Business Card

See description
Note: The name Varrowen is a Chinook word that means 'Friend'. Please do not associate the name with the Whale that shows up on 99% of google searches.

Logo Text

Varrowen Home Inspections

Colors

Designer to choose colors to be used in the design.

Requirements
Must have
• Phone Num: 541-276-8103
• Address: 712 SW 94th Av Num 318
• Portland, Oregon 97185
• Email: mark@varrowenhomeinspection.example
• Website: www.VarrowenHomeInspection.example
• Additional Note: Need to add the Bexolora logo (icon). It should be small and not the focus of the card. The logo can be found at Bexolora.example
Nice to have
• I am open
Should not have
• Cant think of anything

```html
<!DOCTYPE html>
<html lang="en">
<head>
<meta charset="utf-8">
<title>Varrowen Home Inspection – Business Card</title>
<link href="https://fonts.googleapis.com/css2?family=Cinzel:wght@600;700&family=Tinos&display=swap" rel="stylesheet">
<style>
  :root {
    --page: #e9e7e3;
    --card: #2a2929;
    --accent: #f6a41b;
    --grey: #8c8c8c;
    --ink: #ffffff;
    --photo-top: #3a3a36;
    --photo-bottom: #8f9682;
    --seal: #d9b84a;
    --seal-ring: #2e4f9c;
  }
  * { margin: 0; padding: 0; box-sizing: border-box; }
  html, body { width: 1200px; height: 900px; overflow: hidden; background: var(--page); }
  .canvas { position: relative; width: 1200px; height: 900px; }
  .card {
    position: absolute; left: 240px; width: 720px; height: 411px;
    background: var(--card); overflow: hidden;
    box-shadow: 0 6px 18px rgba(0,0,0,.25);
  }
  .card--back { top: 26px; }
  .card--front { top: 463px; }

  .brand { display: flex; align-items: center; gap: 12px; }
  .brand__mark { width: 18px; height: 18px; background: var(--accent); }
  .brand__name {
    font-family: "Cinzel", serif; font-weight: 700; color: var(--accent);
    letter-spacing: 2px; line-height: 1.05;
  }

  .card--back .brand { position: absolute; top: 140px; left: 0; right: 0; justify-content: center; }
  .card--back .brand__name { font-size: 34px; text-align: center; }
  .card--back .address {
    position: absolute; top: 262px; left: 0; right: 0; text-align: center;
    font-family: "Tinos", serif; font-size: 17px; color: var(--ink);
  }

  .card--front .brand { position: absolute; top: 36px; left: 40px; }
  .card--front .brand__name { font-size: 30px; }
  .person { position: absolute; top: 112px; left: 40px; }
  .person__name {
    font-family: "Cinzel", serif; font-weight: 600; font-size: 24px;
    color: var(--ink); letter-spacing: 1.5px;
  }
  .person__role {
    font-family: "Cinzel", serif; font-weight: 600; font-size: 16px;
    color: var(--accent); letter-spacing: 1.5px; margin-top: 2px;
  }
  .contact {
    position: absolute; top: 196px; left: 40px; list-style: none;
    font-family: "Tinos", serif; font-size: 16px; color: var(--ink); line-height: 24px;
  }
  .contact li { display: flex; align-items: center; gap: 8px; }
  .contact svg { width: 14px; height: 14px; flex: none; }
  .contact .plain { padding-left: 0; }

  .portrait {
    position: absolute; right: 0; bottom: 0; width: 330px; height: 300px;
    background: linear-gradient(180deg, var(--photo-top) 0%, var(--photo-bottom) 70%);
    border-top-left-radius: 160px 140px;
  }
  .seal {
    position: absolute; right: 40px; bottom: 22px; width: 70px; height: 70px;
    border-radius: 50%; background: var(--seal); border: 5px solid var(--seal-ring);
  }
</style>
</head>
<body>
<main class="canvas">

  <section class="card card--back" aria-label="Business card back">
    <div class="brand">
      <span class="brand__mark"></span>
      <span class="brand__name">VARROWEN<br>HOME INSPECTION</span>
    </div>
    <p class="address">712 SW 94th Av Num 318, Portland, Oregon 97185</p>
  </section>

  <section class="card card--front" aria-label="Business card front">
    <div class="brand">
      <span class="brand__mark"></span>
      <span class="brand__name">VARROWEN HOME INSPECTION</span>
    </div>

    <div class="person">
      <p class="person__name">YOUR FULL NAME HERE</p>
      <p class="person__role">MANAGING DERECTOR</p>
    </div>

    <ul class="contact">
      <li class="plain">712 SW 94th Av Num 318</li>
      <li class="plain">Portland, Oregon 97185</li>
      <li>
        <svg viewBox="0 0 16 16" aria-hidden="true"><path d="M4 1l3 3-2 2c1 2 3 4 5 5l2-2 3 3-2 3C7 15 1 9 1 3z" fill="var(--accent)"/></svg>
        541-276-8103
      </li>
      <li>
        <svg viewBox="0 0 16 16" aria-hidden="true"><rect x="1" y="3" width="14" height="10" fill="var(--accent)"/><path d="M1 3l7 6 7-6" fill="none" stroke="var(--card)" stroke-width="1.4"/></svg>
        mark@varrowenhomeinspection.example
      </li>
      <li>
        <svg viewBox="0 0 16 16" aria-hidden="true"><circle cx="8" cy="8" r="6.5" fill="none" stroke="var(--accent)" stroke-width="1.5"/><path d="M1.5 8h13M8 1.5c-3 3-3 10 0 13M8 1.5c3 3 3 10 0 13" fill="none" stroke="var(--accent)" stroke-width="1.2"/></svg>
        www.VarrowenHomeInspection.example
      </li>
    </ul>

    <div class="portrait" role="img" aria-label="Portrait photo of the inspector in a green work shirt"></div>
    <div class="seal" role="img" aria-label="Bexolora certification badge"></div>
  </section>

</main>
</body>
</html>
```